I need creative and unique business card design using my company logo. Ok to change logo color. We are a small brokerage doing both Real Estate and Mortgage services. Need to have the follow on business card;
1. agent name - Mila Fenton - Realtor
2. cell - 949-555-0182
3. license number - DRE 04917362
4. business name - Brightway Estates & Lending, Inc
5. business office - 626-555-0147
6. business address - 287 W. Larkmoor Ave #214, Arcadia CA 91088
7. business logo - attached (ok to use different color on logo)

```html
<!DOCTYPE html>
<html lang="en">
<head>
<meta charset="utf-8">
<title>Brightway Estates &amp; Lending – Business Card</title>
<link href="https://fonts.googleapis.com/css2?family=Arimo:wght@400;700&display=swap" rel="stylesheet">
<style>
  :root {
    --backdrop: #3a3a3a;
    --blue-deep: #2554a3;
    --blue-mid: #3471bb;
    --blue-light: #52a5dd;
    --ink: #111111;
    --paper: #ffffff;
    --rule-grey: #b5b5b5;
  }
  * { box-sizing: border-box; margin: 0; padding: 0; }
  html, body {
    width: 1200px; height: 689px; overflow: hidden;
    background: var(--backdrop);
    font-family: "Arimo", Arial, sans-serif;
  }
  .stage {
    position: relative; width: 1200px; height: 689px;
    display: flex; align-items: center; justify-content: center; gap: 40px;
  }
  .card {
    position: relative; width: 540px; height: 309px; overflow: hidden;
    box-shadow: 0 14px 30px rgba(0,0,0,.45);
  }

  /* Front */
  .card-front {
    background: linear-gradient(120deg, var(--blue-mid) 0%, var(--blue-light) 45%, var(--blue-deep) 100%);
    display: flex; align-items: center; justify-content: center;
  }
  .brand {
    display: flex; align-items: center; gap: 12px;
    font-family: "Arimo", Arial, sans-serif; font-weight: 400;
  }
  .brand-mark { flex: none; }
  .card-front .brand-name { color: var(--paper); font-size: 22px; line-height: 1.25; }
  .card-front .brand-mark { width: 46px; height: 46px; background: var(--paper); }

  /* Back */
  .card-back { background: var(--paper); }
  .swoosh { position: absolute; inset: 0; }
  .card-back .brand {
    position: absolute; left: 34px; top: 98px; width: 200px;
  }
  .card-back .brand-mark { width: 30px; height: 30px; background: var(--blue-deep); }
  .card-back .brand-name { color: var(--blue-deep); font-size: 15px; line-height: 1.3; }
  .divider {
    position: absolute; left: 252px; top: 40px; width: 1.5px; height: 160px;
    background: var(--blue-deep);
  }
  .contact {
    position: absolute; left: 268px; top: 38px;
    color: var(--ink); font-size: 12.5px; line-height: 1.35;
  }
  .agent-name { font-size: 21px; font-weight: 700; letter-spacing: .3px; line-height: 1.1; }
  .agent-name .first { color: var(--blue-deep); }
  .agent-name .last { color: var(--blue-light); }
  .agent-title { margin-bottom: 6px; }
  .phone-line { display: flex; align-items: center; gap: 6px; }
  .phone-line svg { width: 12px; height: 12px; fill: var(--blue-deep); }
</style>
</head>
<body>
<main class="stage">

  <section class="card card-front" aria-label="Card front">
    <div class="brand">
      <span class="brand-mark"></span>
      <span class="brand-name">Brightway Estates<br>&amp; Lending, Inc</span>
    </div>
  </section>

  <section class="card card-back" aria-label="Card back">
    <svg class="swoosh" viewBox="0 0 540 309" preserveAspectRatio="none" aria-hidden="true">
      <defs>
        <linearGradient id="swooshFill" x1="0" y1="1" x2="1" y2="0">
          <stop offset="0" stop-color="#2554a3"/>
          <stop offset=".55" stop-color="#52a5dd"/>
          <stop offset="1" stop-color="#2554a3"/>
        </linearGradient>
      </defs>
      <path d="M0,272 Q330,255 540,100 L540,309 L0,309 Z" fill="url(#swooshFill)"/>
      <path d="M120,258 Q390,232 522,118" fill="none" stroke="#b5b5b5" stroke-width="3"/>
    </svg>

    <div class="brand">
      <span class="brand-mark"></span>
      <span class="brand-name">Brightway Estates<br>&amp; Lending, Inc</span>
    </div>

    <div class="divider"></div>

    <div class="contact">
      <p class="agent-name"><span class="first">MILA</span> <span class="last">FENTON</span></p>
      <p class="agent-title">Realtor</p>
      <p>Brightway Estates &amp; Lending, Inc</p>
      <p>287 W. Larkmoor Ave</p>
      <p>#214, Arcadia CA 91088</p>
      <p class="phone-line">
        <svg viewBox="0 0 24 24" aria-hidden="true"><path d="M6.6 10.8a15 15 0 0 0 6.6 6.6l2.2-2.2c.3-.3.7-.4 1-.2 1.1.4 2.3.6 3.6.6.6 0 1 .4 1 1V20c0 .6-.4 1-1 1A17 17 0 0 1 3 4c0-.6.4-1 1-1h3.5c.6 0 1 .4 1 1 0 1.3.2 2.5.6 3.6.1.3 0 .7-.2 1z"/></svg>
        949-555-0182
      </p>
      <p class="phone-line">
        <svg viewBox="0 0 24 24" aria-hidden="true"><path d="M3 9c5-5 13-5 18 0l-2.5 3-3-1.5V8.5a10 10 0 0 0-7 0v2L5.5 12zM6 14h12l1.5 6h-15z"/></svg>
        626-555-0147
      </p>
      <p>DRE 04917362</p>
    </div>
  </section>

</main>
</body>
</html>
```